"Willow Drift" Mattress Pad Packaging

We need packaging for a mattress pad. This will be sold through retailers across North America. We need something modern and clean, an update from what we currently have. This is targeted towards older women. I've attached what our current packaging looks like as well as other mattress pad packaging. This is a simple product so we're open to creativity and experimentation. This is our first time using this site so we're very open and hoping for something fun.

Font styles to use
Serif
Sans Serif

Colors

Designer to choose colors to be used in the design.

```html
<!DOCTYPE html>
<html lang="en">
<head>
<meta charset="utf-8">
<title>Willow Drift Mattress Pad Packaging</title>
<link rel="stylesheet" href="https://fonts.googleapis.com/css2?family=Cinzel:wght@400;600;700&display=swap">
<style>
  :root {
    --backdrop: #c8ced2;
    --forest: #2c5a37;
    --forest-deep: #24492d;
    --salmon: #e0937c;
    --cream: #f2e4c4;
  }
  * { margin: 0; padding: 0; box-sizing: border-box; }
  html, body { width: 748px; height: 1200px; overflow: hidden; }
  body {
    background: var(--backdrop);
    font-family: "Cinzel", Georgia, serif;
    color: var(--cream);
    position: relative;
  }
  .package-label {
    position: absolute;
    left: 169px;
    width: 410px;
    height: 476px;
    background: var(--forest);
    overflow: hidden;
  }
  .label-front { top: 99px; }
  .label-alt { top: 600px; }
  .label-art {
    position: absolute; inset: 0;
    width: 410px; height: 476px;
  }
  .brand-mark {
    position: absolute; left: 50%;
    width: 52px; height: 52px;
    margin-left: -26px;
    border: 2px solid var(--cream);
    border-radius: 50%;
  }
  .brand-name {
    position: absolute; left: 0; right: 0;
    text-align: center;
    font-size: 31px; font-weight: 400;
    letter-spacing: 1px;
  }
  .collection-name {
    position: absolute; left: 0; right: 0;
    text-align: center;
    font-size: 14px; font-weight: 400;
    letter-spacing: 1.5px;
  }
  .divider-rule {
    position: absolute; left: 50%;
    width: 170px; height: 1px;
    margin-left: -85px;
    background: var(--cream);
  }
  .rating-stars {
    position: absolute; left: 50%;
    width: 90px; margin-left: -45px;
    height: 16px;
  }
  .feature-list {
    position: absolute; left: 0; right: 0;
    list-style: none;
    text-align: center;
    font-size: 13px; font-weight: 700;
    letter-spacing: 1px;
  }
  .feature-list li { height: 30px; line-height: 30px; }
</style>
</head>
<body>

  <section class="package-label label-front">
    <svg class="label-art" viewBox="0 0 410 476" aria-hidden="false">
      <rect width="410" height="476" fill="var(--forest)" role="img" aria-label="Dark green repeating floral lattice pattern"/>
      <path d="M30,-2 q6,10 0,20 t0,20 t0,20 t0,20 t0,20 t0,20 t0,20 t0,20 t0,20 t0,20 t0,20 t0,20 t0,20 t0,20 t0,20 t0,20 t0,20 t0,20 t0,20 t0,20 t0,20 t0,20 t0,20 t0,20" fill="none" stroke="var(--salmon)" stroke-width="3"/>
      <path d="M380,-2 q6,10 0,20 t0,20 t0,20 t0,20 t0,20 t0,20 t0,20 t0,20 t0,20 t0,20 t0,20 t0,20 t0,20 t0,20 t0,20 t0,20 t0,20 t0,20 t0,20 t0,20 t0,20 t0,20 t0,20 t0,20" fill="none" stroke="var(--salmon)" stroke-width="3"/>
    </svg>
    <div class="brand-mark" style="top:48px"></div>
    <h1 class="brand-name" style="top:203px">WILLOW DRIFT</h1>
    <p class="collection-name" style="top:250px">HAUTE COLLECTION</p>
    <div class="divider-rule" style="top:290px"></div>
    <ul class="feature-list" style="top:317px">
      <li>300 THREAD COUNT</li>
      <li>STRETCH-TO-FIT-SKIRT</li>
      <li>ALLERGY DETERRENT</li>
      <li>100% COTTON</li>
    </ul>
  </section>

  <section class="package-label label-alt">
    <svg class="label-art" viewBox="0 0 410 476">
      <rect width="410" height="476" fill="var(--forest)" role="img" aria-label="Dark green repeating floral lattice pattern"/>
      <path d="M0,0 L42,0 L42,-2 q6,10 0,20 t0,20 t0,20 t0,20 t0,20 t0,20 t0,20 t0,20 t0,20 t0,20 t0,20 t0,20 t0,20 t0,20 t0,20 t0,20 t0,20 t0,20 t0,20 t0,20 t0,20 t0,20 t0,20 t0,20 L0,478 Z" fill="var(--salmon)"/>
      <path d="M410,0 L368,0 L368,-2 q6,10 0,20 t0,20 t0,20 t0,20 t0,20 t0,20 t0,20 t0,20 t0,20 t0,20 t0,20 t0,20 t0,20 t0,20 t0,20 t0,20 t0,20 t0,20 t0,20 t0,20 t0,20 t0,20 t0,20 t0,20 L410,478 Z" fill="var(--salmon)"/>
    </svg>
    <div class="brand-mark" style="top:73px"></div>
    <h2 class="brand-name" style="top:201px">WILLOW DRIFT</h2>
    <p class="collection-name" style="top:248px">HAUTE COLLECTION</p>
    <svg class="rating-stars" style="top:284px" viewBox="0 0 90 16" role="img" aria-label="Five stars">
      <g fill="var(--cream)">
        <path id="star" d="M8,0 L10,5.5 L16,5.8 L11.3,9.5 L13,15.5 L8,12 L3,15.5 L4.7,9.5 L0,5.8 L6,5.5 Z"/>
        <use href="#star" x="18.5"/>
        <use href="#star" x="37"/>
        <use href="#star" x="55.5"/>
        <use href="#star" x="74"/>
      </g>
    </svg>
    <ul class="feature-list" style="top:322px">
      <li>300 THREAD COUNT</li>
      <li>STRETCH-TO-FIT-SKIRT</li>
      <li>ALLERGY DETERRENT</li>
      <li>100% COTTON</li>
    </ul>
  </section>

</body>
</html>
```